Master slides for standard ppt presentation

I just my company, went through Quillmarks for the log design and already have an identity that I like.
I need to transpose this identity into some nice Master slides for Powerpoint presentation. I want it clean, with fresh color connection to my logo, not over crowded and obviously different vs what powerpoint proposes as standard design ideas. I will attach a few materials that I already use, branded with the company logo so that you can take inspiration.

```html
<!DOCTYPE html>
<html lang="en">
<head>
<meta charset="utf-8">
<title>NOVALYNE Master Slides</title>
<link href="https://fonts.googleapis.com/css2?family=Roboto:wght@300;400;500;700&family=Roboto+Condensed:wght@300;400;700&display=swap" rel="stylesheet">
<style>
:root{
  --deep:#0b4a3c;
  --teal:#0e9e80;
  --mint:#1fd48e;
  --lime:#5cc84a;
  --slate:#4a5560;
  --gray:#7d8894;
  --ink:#2f3438;
  --body:#8a9096;
  --page:#ffffff;
}
*{margin:0;padding:0;box-sizing:border-box}
html,body{width:1200px;height:1200px;overflow:hidden;background:var(--page)}
body{position:relative;font-family:"Roboto",sans-serif;color:var(--ink)}
.slide{position:absolute;width:325px;height:183px;background:#fff;overflow:hidden;box-shadow:3px 4px 10px rgba(0,0,0,.22)}
.abs{position:absolute}
.title{position:absolute;font-family:"Roboto",sans-serif;font-weight:500;color:var(--ink);font-size:10px;line-height:12.5px;letter-spacing:-.1px}
.sub{position:absolute;font-family:"Roboto Condensed",sans-serif;font-size:5px;color:#555}
.text{position:absolute;font-family:"Roboto Condensed",sans-serif;font-weight:300;font-size:2.6px;line-height:3.7px;color:var(--body)}
.text p+p{margin-top:3px}
.footer{position:absolute;left:0;right:0;bottom:7px;height:4px;font-family:"Roboto Condensed",sans-serif;font-size:3px}
.footer .brand{position:absolute;left:27px;font-weight:700;color:var(--deep)}
.footer .link{position:absolute;left:0;right:0;text-align:center;color:var(--teal)}
.footer .num{position:absolute;right:27px;color:var(--gray)}
.mark{position:absolute;right:17px;top:11px;display:flex;align-items:center;gap:2px;font-weight:700;font-size:4.5px;color:var(--teal);letter-spacing:.2px}
.mark i{display:block;width:6px;height:6px;border-radius:50%;background:var(--mint)}
.photo-city{background:linear-gradient(180deg,#d4dce2 0%,#9aa7b1 45%,#56626c 75%,#37424b 100%)}
.photo-bridge{background:linear-gradient(180deg,#c3d0da 0%,#9db2c2 28%,#5a84a3 45%,#2f5e82 70%,#24506f 100%)}
.photo-sunset{background:linear-gradient(180deg,#f4b46a 0%,#e0813f 40%,#8c5540 70%,#3c3a44 100%)}
.box{position:absolute;color:#fff;padding:5px 6px;font-family:"Roboto Condensed",sans-serif}
.box .date{font-size:2.8px;opacity:.9}
.box .bt{font-size:3.2px;font-weight:700;margin:1px 0 3px}
.box .bb{font-size:2.6px;line-height:3.6px;font-weight:300}
.bg-deep{background:var(--deep)}
.bg-teal{background:var(--teal)}
.bg-mint{background:var(--mint)}
.bg-lime{background:var(--lime)}
.item{position:absolute;width:120px;height:20px}
.item .ic{position:absolute;left:0;top:0;width:11px;height:11px;border-radius:50%}
.item .ic svg{width:11px;height:11px}
.item .it{position:absolute;left:28px;top:0;font-size:3.4px;font-weight:700;color:var(--ink)}
.item .ib{position:absolute;left:28px;top:4.5px;width:85px;font-family:"Roboto Condensed",sans-serif;font-size:3.2px;line-height:4.3px;color:var(--body)}
.card{position:absolute;top:55px;width:64px;height:98px;color:#fff;font-family:"Roboto Condensed",sans-serif}
.card .ph{height:37px;border-bottom:1px solid #fff}
.card .price{position:absolute;left:8px;top:50px;font-family:"Roboto",sans-serif;font-size:8px;font-weight:700}
.card .price small{font-size:2.8px;font-weight:400}
.card .tier{position:absolute;left:8px;top:62px;font-size:3px;font-weight:700}
.card .desc{position:absolute;left:8px;top:66px;width:50px;font-size:2.7px;line-height:3.6px;font-weight:300}
.bullets{position:absolute;font-family:"Roboto Condensed",sans-serif;font-size:2.6px;line-height:3.6px;color:var(--body);padding-left:5px}
.bullets li{margin-bottom:1px}
.axis{font-family:"Roboto Condensed",sans-serif;font-size:2.6px;fill:#8a9096}
</style>
</head>
<body>

<!-- 1 cover -->
<section class="slide" style="left:56px;top:94px">
  <div class="abs" style="left:36px;top:60px;display:flex;align-items:center;gap:6px;font-weight:700;font-size:15px;color:var(--teal)">
    <span style="width:22px;height:22px;border-radius:50%;background:var(--mint);display:block"></span>NOVALYNE
  </div>
  <div class="abs" style="left:192px;top:35px;width:1px;height:110px;background:var(--teal)"></div>
  <h1 class="abs" style="left:203px;top:46px;font-size:13.5px;line-height:16.4px;font-weight:700;color:var(--deep)">NOVALYNE<br>Company<br>Business<br>Presentation</h1>
  <div class="abs" style="left:203px;top:114px;font-family:'Roboto Condensed',sans-serif;font-size:6.5px;color:#444">Marc Delorme</div>
  <div class="abs" style="left:203px;top:124px;font-family:'Roboto Condensed',sans-serif;font-size:3.2px;color:#666">CEO - FOUNDER</div>
  <div class="abs" style="left:203px;top:133px;font-family:'Roboto Condensed',sans-serif;font-size:3.2px;color:#666">Sep 2023</div>
  <div class="abs" style="left:0;right:0;top:174px;text-align:center;font-size:3.2px;letter-spacing:2.2px;color:#666">marc.delorme@novalyne.com</div>
</section>

<!-- 2 welcome -->
<section class="slide" style="left:443px;top:94px">
  <div class="abs photo-bridge" role="img" aria-label="Aerial photo of a cable-stayed bridge over a bay" style="left:0;top:0;width:325px;height:84px"></div>
  <div class="abs" style="left:23px;top:61px;font-weight:700;font-size:8px;color:#fff;letter-spacing:.3px">NOVALYNE</div>
  <div class="abs" style="left:0;right:0;top:94px;text-align:center;font-size:10px;font-weight:500">Welcome Message</div>
  <div class="abs" style="left:0;right:0;top:110px;text-align:center;font-size:4.5px;font-weight:500">Presentation By:</div>
  <div class="abs" style="left:0;right:0;top:120px;text-align:center;font-family:'Roboto Condensed',sans-serif;font-size:7px;color:var(--deep)">Marc Delorme CEO - FOUNDER</div>
  <div class="text" style="left:29px;top:136px;width:270px">Lorem ipsum is simply dummy text of the printing and typesetting industry, used as standard filler since the early days of print. It has survived many decades and the leap into electronic layout, remaining essentially unchanged. It was made popular with sheets of transfer letters and later with desktop publishing software that still uses it today. Contrary to popular belief it is not simply random text, it has roots in classical literature.</div>
  <div class="footer"><span class="brand">NOVALYNE</span><span class="link">brand page/novalyne</span><span class="num">2</span></div>
</section>

<!-- 3 services tiles -->
<section class="slide" style="left:826px;top:94px">
  <div class="mark"><i></i>NOVALYNE</div>
  <h2 class="title" style="left:27px;top:26px">Our Business Creative Services and Solutions.</h2>
  <div class="text" style="left:27px;top:41px;width:270px">Lorem ipsum is simply dummy text of the printing and typesetting industry, used as standard filler since the early days of print. It has survived many decades and the leap into electronic layout, remaining essentially unchanged. It was made popular with sheets of transfer letters and later with desktop publishing software. It is a long established fact that a reader will be distracted by the readable content of a page when looking at its layout. The point of using it is a more or less normal distribution of letters, making it look like readable English. Many publishing packages now use it as their default model text.</div>
  <div class="abs photo-city" role="img" aria-label="City skyscrapers photo" style="left:27px;top:91px;width:66px;height:63px"></div>
  <div class="box bg-deep" style="left:95px;top:91px;width:66px;height:63px;padding-top:30px"><div class="bt">BUSINESS MEET ROOM</div><div class="bb">Lorem ipsum is simply dummy text of the printing and typesetting industry.</div></div>
  <div class="abs photo-city" role="img" aria-label="Downtown city towers photo" style="left:163px;top:91px;width:66px;height:63px;background:linear-gradient(180deg,#cdd8e0,#a58f6c 55%,#4e4a44)"></div>
  <div class="box bg-teal" style="left:231px;top:91px;width:66px;height:63px;padding-top:30px"><div class="bt">BRANDING SOLUTIONS</div><div class="bb">Lorem ipsum is simply dummy text of the printing and typesetting industry.</div></div>
  <div class="footer"><span class="brand">NOVALYNE</span><span class="link">brand page/novalyne</span><span class="num">3</span></div>
</section>

<!-- 4 services icons -->
<section class="slide" style="left:56px;top:303px">
  <div class="mark"><i></i>NOVALYNE</div>
  <h2 class="title" style="left:27px;top:26px">Our Business Creative Services and Solutions.</h2>
  <div class="item" style="left:31px;top:53px"><span class="ic" style="background:var(--deep)"><svg viewBox="0 0 11 11"><rect x="3" y="3" width="5" height="5" rx="1" fill="#fff"/></svg></span><div class="it">Business Services and Solutions.</div><div class="ib">Lorem ipsum is simply dummy text of the printing and typesetting industry.</div></div>
  <div class="item" style="left:31px;top:87px"><span class="ic" style="background:var(--lime)"><svg viewBox="0 0 11 11"><circle cx="5.5" cy="5" r="2.3" fill="#fff"/></svg></span><div class="it">Business Services and Solutions.</div><div class="ib">Lorem ipsum is simply dummy text of the printing and typesetting industry.</div></div>
  <div class="item" style="left:31px;top:120px"><span class="ic" style="background:var(--slate)"><svg viewBox="0 0 11 11"><circle cx="5.5" cy="5.5" r="2.3" fill="none" stroke="#fff" stroke-width="1"/></svg></span><div class="it">Business Services and Solutions.</div><div class="ib">Lorem ipsum is simply dummy text of the printing and typesetting industry.</div></div>
  <div class="item" style="left:172px;top:53px"><span class="ic" style="background:var(--mint)"><svg viewBox="0 0 11 11"><ellipse cx="5.5" cy="5.5" rx="3" ry="1.8" fill="none" stroke="#fff" stroke-width=".8"/><circle cx="5.5" cy="5.5" r=".9" fill="#fff"/></svg></span><div class="it">Business Services and Solutions.</div><div class="ib">Lorem ipsum is simply dummy text of the printing and typesetting industry.</div></div>
  <div class="item" style="left:172px;top:87px"><span class="ic" style="background:var(--slate)"><svg viewBox="0 0 11 11"><circle cx="5.5" cy="5" r="2" fill="none" stroke="#fff" stroke-width=".8"/><rect x="4.6" y="7.2" width="1.8" height="1" fill="#fff"/></svg></span><div class="it">Business Services and Solutions.</div><div class="ib">Lorem ipsum is simply dummy text of the printing and typesetting industry.</div></div>
  <div class="item" style="left:172px;top:120px"><span class="ic" style="background:var(--mint)"><svg viewBox="0 0 11 11"><circle cx="5.5" cy="5.5" r="2.5" fill="none" stroke="#fff" stroke-width=".9"/></svg></span><div class="it">Business Services and Solutions.</div><div class="ib">Lorem ipsum is simply dummy text of the printing and typesetting industry.</div></div>
  <div class="footer"><span class="brand">NOVALYNE</span><span class="link">brand page/novalyne</span><span class="num">4</span></div>
</section>

<!-- 5 events grid -->
<section class="slide" style="left:443px;top:303px">
  <div class="abs photo-city" role="img" aria-label="Tall city skyline photo" style="left:27px;top:18px;width:123px;height:146px"></div>
  <div class="abs" style="left:40px;top:112px;font-weight:700;font-size:9px;color:#fff">NOVALYNE</div>
  <div class="box bg-mint" style="left:151px;top:18px;width:97px;height:49px"><div class="date">August 08, 2023</div><div class="bt">Technology Marketing Event</div><div class="bb">Lorem ipsum is simply dummy text of the printing and typesetting industry, used as standard filler since the early days of print.</div></div>
  <div class="abs photo-city" role="img" aria-label="Skyscraper cluster photo" style="left:249px;top:18px;width:49px;height:49px"></div>
  <div class="abs photo-sunset" role="img" aria-label="Bridge at sunset photo" style="left:151px;top:68px;width:48px;height:48px"></div>
  <div class="box bg-deep" style="left:200px;top:68px;width:98px;height:48px"><div class="date">May 05, 2023</div><div class="bt">Design Business Center</div><div class="bb">Lorem ipsum is simply dummy text of the printing and typesetting industry, used as standard filler since the early days of print.</div></div>
  <div class="box bg-teal" style="left:151px;top:117px;width:97px;height:47px"><div class="date">April 26, 2023</div><div class="bt">Business Services and Solutions.</div><div class="bb">Lorem ipsum is simply dummy text of the printing and typesetting industry, used as standard filler since the early days of print.</div></div>
  <div class="abs photo-bridge" role="img" aria-label="Bridge over water photo" style="left:249px;top:117px;width:49px;height:47px"></div>
  <div class="footer"><span class="brand">NOVALYNE</span><span class="link">brand page/novalyne</span><span class="num">5</span></div>
</section>

<!-- 6 single column -->
<section class="slide" style="left:826px;top:303px">
  <div class="mark"><i></i>NOVALYNE</div>
  <h2 class="title" style="left:28px;top:29px">Single Column Text Layout.</h2>
  <div class="sub" style="left:28px;top:44px">Lorem Ipsum is simply dummy text of the printing and typesetting industry</div>
  <div class="text" style="left:28px;top:57px;width:270px">
    <p>Lorem ipsum is simply dummy text of the printing and typesetting industry, used as standard filler since the early days of print. It has survived many decades and the leap into electronic layout, remaining essentially unchanged. It was made popular with sheets of transfer letters and later with desktop publishing software that still uses it today.</p>
    <p>It is a long established fact that a reader will be distracted by the readable content of a page when looking at its layout. The point of using it is a more or less normal distribution of letters, as opposed to plain repeated content, making it look like readable English. Many publishing packages now use it as their default model text, and a search will uncover many sites still in their infancy.</p>
    <p>Contrary to popular belief, it is not simply random text. It has roots in a piece of classical literature, making it over two thousand years old. A professor looked up one of the more obscure words and went through the cites of the word in classical literature, discovering its source in a treatise on ethics that was very popular during the renaissance.</p>
    <p>The standard chunk used since the early days is reproduced below for those interested, accompanied by English versions from a later translation.</p>
  </div>
  <div class="footer"><span class="brand">NOVALYNE</span><span class="link">brand page/novalyne</span><span class="num">6</span></div>
</section>

<!-- 7 two columns -->
<section class="slide" style="left:56px;top:512px">
  <div class="mark"><i></i>NOVALYNE</div>
  <h2 class="title" style="left:28px;top:29px">Single Column Text Layout.</h2>
  <div class="sub" style="left:28px;top:44px">Lorem Ipsum is simply dummy text of the printing and typesetting industry</div>
  <div class="text" style="left:28px;top:58px;width:119px">
    <p>Lorem ipsum is simply dummy text of the printing and typesetting industry, used as standard filler since the early days of print. It has survived many decades and the leap into electronic layout, remaining essentially unchanged. It was made popular with sheets of transfer letters and later with desktop publishing software.</p>
    <p>It is a long established fact that a reader will be distracted by the readable content of a page when looking at its layout. The point of using it is a more or less normal distribution of letters, making it look like readable English. Many publishing packages now use it as their default model text, and many sites are still in their infancy.</p>
  </div>
  <div class="text" style="left:176px;top:58px;width:119px">
    <p>Lorem ipsum is simply dummy text of the printing and typesetting industry, used as standard filler since the early days of print. It has survived many decades and the leap into electronic layout, remaining essentially unchanged. It was made popular with sheets of transfer letters and later with desktop publishing software.</p>
    <p>It is a long established fact that a reader will be distracted by the readable content of a page when looking at its layout. The point of using it is a more or less normal distribution of letters, making it look like readable English. Many publishing packages now use it as their default model text, and many sites are still in their infancy.</p>
  </div>
  <div class="footer"><span class="brand">NOVALYNE</span><span class="link">brand page/novalyne</span><span class="num">7</span></div>
</section>

<!-- 8 full image -->
<section class="slide" style="left:443px;top:512px">
  <div class="abs photo-bridge" role="img" aria-label="Aerial photo of a cable-stayed bridge over a bay" style="left:0;top:0;width:325px;height:126px"></div>
  <div class="mark"><i></i>NOVALYNE</div>
  <h2 class="title" style="left:26px;top:134px;font-size:10.5px;line-height:13px">Title of One Full Image Project<br>&amp; Additional Text Description</h2>
  <div class="box bg-teal" style="left:200px;top:91px;width:88px;height:92px;padding:9px 6px"><div style="font-size:5.5px;font-weight:700;font-family:'Roboto',sans-serif;margin-bottom:3px">Your Subtitle Slide</div><div class="bb">Lorem ipsum is simply dummy text of the printing and typesetting industry, used as standard filler since the early days of print. It has survived many decades and the leap into electronic layout, remaining essentially unchanged. It was made popular with sheets of transfer letters and later with desktop software.</div></div>
  <div class="footer"><span class="brand">NOVALYNE</span><span class="link" style="right:130px">brand page/novalyne</span><span class="num" style="right:27px">8</span></div>
</section>

<!-- 9 subtitle grid -->
<section class="slide" style="left:826px;top:512px">
  <div class="mark" style="left:28px;right:auto"><i></i>NOVALYNE</div>
  <h2 class="title" style="left:27px;top:34px">Our Business Creative<br>Services and Solutions.</h2>
  <div class="text" style="left:27px;top:65px;width:113px">Lorem ipsum is simply dummy text of the printing and typesetting industry, used as standard filler since the early days of print. It has survived many decades and the leap into electronic layout, remaining essentially unchanged. It was made popular with sheets of transfer letters and later with desktop publishing software.</div>
  <svg class="abs" style="left:27px;top:120px" width="110" height="40" viewBox="0 0 110 40">
    <circle cx="12" cy="9" r="8" fill="var(--deep)"/><circle cx="54" cy="9" r="8" fill="var(--slate)"/><circle cx="96" cy="9" r="8" fill="var(--mint)"/>
    <circle cx="12" cy="8" r="2" fill="#fff"/><circle cx="54" cy="9" r="3.5" fill="none" stroke="#fff" stroke-width="1.2"/>
    <rect x="93" y="7" width="1.5" height="5" fill="#fff"/><rect x="95.5" y="5" width="1.5" height="7" fill="#fff"/><rect x="98" y="8" width="1.5" height="4" fill="#fff"/>
    <text x="12" y="23" text-anchor="middle" font-size="3.6" font-weight="500" fill="#333" font-family="Roboto,sans-serif">Your Subtitle</text>
    <text x="54" y="23" text-anchor="middle" font-size="3.6" font-weight="500" fill="#333" font-family="Roboto,sans-serif">Your Subtitle</text>
    <text x="96" y="23" text-anchor="middle" font-size="3.6" font-weight="500" fill="#333" font-family="Roboto,sans-serif">Your Subtitle</text>
  </svg>
  <div class="abs photo-city" role="img" aria-label="Skyscrapers photo divided into a grid" style="left:151px;top:18px;width:147px;height:146px;background:linear-gradient(180deg,#e2e8ec 0%,#b9c4cb 40%,#6a7680 70%,#3e4850 100%)"></div>
  <svg class="abs" style="left:151px;top:18px" width="147" height="146"><g stroke="#fff" stroke-width=".8"><line x1="37" y1="0" x2="37" y2="146"/><line x1="74" y1="0" x2="74" y2="146"/><line x1="111" y1="0" x2="111" y2="146"/><line x1="0" y1="36" x2="147" y2="36"/><line x1="0" y1="73" x2="147" y2="73"/><line x1="0" y1="110" x2="147" y2="110"/></g></svg>
  <div class="box bg-teal" style="left:226px;top:92px;width:72px;height:72px;padding:8px 7px"><div style="font-size:5px;font-weight:700;font-family:'Roboto',sans-serif;margin-bottom:3px">Your Subtitle Slide</div><div class="bb">Lorem ipsum is simply dummy text of the printing and typesetting industry, used as standard filler since the early days of print and layout.</div></div>
  <div class="footer"><span class="brand">NOVALYNE</span><span class="link">brand page/novalyne</span><span class="num">9</span></div>
</section>

<!-- 10 price table -->
<section class="slide" style="left:56px;top:722px">
  <div class="mark"><i></i>NOVALYNE</div>
  <h2 class="title" style="left:27px;top:33px">Business &amp; Image Service Price Table</h2>
  <div class="card bg-deep" style="left:27px"><div class="ph photo-city" role="img" aria-label="City skyline photo"></div><div class="price">$1550<small>/ Month</small></div><div class="tier">The Basic User</div><div class="desc">Objectively disintermediate leveraged manufactured products before team driven resources.</div></div>
  <div class="card bg-teal" style="left:96px"><div class="ph photo-city" role="img" aria-label="Office towers photo"></div><div class="price">$2750<small>/ Month</small></div><div class="tier">The Premium User</div><div class="desc">Objectively disintermediate leveraged manufactured products before team driven resources.</div></div>
  <div class="card bg-mint" style="left:165px"><div class="ph photo-bridge" role="img" aria-label="Bridge over water photo"></div><div class="price">$3800<small>/ Month</small></div><div class="tier">The Golden User</div><div class="desc">Objectively disintermediate leveraged manufactured products before team driven resources.</div></div>
  <div class="card bg-lime" style="left:234px"><div class="ph photo-sunset" role="img" aria-label="Bridge at sunset photo"></div><div class="price">$4980<small>/ Month</small></div><div class="tier">The Ultimate User</div><div class="desc">Objectively disintermediate leveraged manufactured products before team driven resources.</div></div>
  <div class="footer"><span class="brand">NOVALYNE</span><span class="link">brand page/novalyne</span><span class="num">10</span></div>
</section>

<!-- 11 pie -->
<section class="slide" style="left:443px;top:722px">
  <div class="mark"><i></i>NOVALYNE</div>
  <h2 class="title" style="left:25px;top:33px">Title for Data Pie Slide<br>Service and Solutions.</h2>
  <div class="text" style="left:25px;top:62px;width:110px">Lorem ipsum is simply dummy text of the printing and typesetting industry, used as standard filler since the early days of print. It has survived many decades and the leap into electronic layout, remaining essentially unchanged. It was made popular with sheets of transfer letters and later with desktop publishing software.</div>
  <ul class="bullets" style="left:25px;top:113px;width:110px">
    <li>It is a long established fact that a reader will be distracted by the readable content of a page.</li>
    <li>The point of using it is a more or less normal distribution of letters, making it look readable.</li>
    <li>Many publishing packages now use it as their default model text.</li>
  </ul>
  <svg class="abs" style="left:150px;top:48px" width="160" height="100" viewBox="0 0 160 100">
    <g transform="translate(80,40) scale(1,.6)">
      <g transform="translate(0,14)">
        <path d="M4,-6 L4,-76 A70,70 0 0 1 70,4 Z" fill="#062e25"/>
        <path d="M6,4 L72,4 A70,70 0 0 1 -30,68 Z" fill="#12a86c"/>
        <path d="M-6,8 L-36,72 A70,70 0 0 1 -72,-6 Z" fill="#0c8f5e"/>
        <path d="M-6,-4 L-74,-10 A70,70 0 0 1 -6,-74 Z" fill="#3a9a2e"/>
      </g>
      <path d="M4,-6 L4,-76 A70,70 0 0 1 70,4 Z" fill="var(--deep)"/>
      <path d="M6,4 L72,4 A70,70 0 0 1 -30,68 Z" fill="#22ee98"/>
      <path d="M-6,8 L-36,72 A70,70 0 0 1 -72,-6 Z" fill="#16cc84"/>
      <path d="M-6,-4 L-74,-10 A70,70 0 0 1 -6,-74 Z" fill="#4cc03e"/>
    </g>
  </svg>
  <div class="footer"><span class="brand">NOVALYNE</span><span class="link">brand page/novalyne</span><span class="num">11</span></div>
</section>

<!-- 12 area chart -->
<section class="slide" style="left:826px;top:722px">
  <div class="mark"><i></i>NOVALYNE</div>
  <h2 class="title" style="left:27px;top:29px">Title for Full Area Data<br>Service and Solutions.</h2>
  <div class="text" style="left:27px;top:58px;width:115px">Lorem ipsum is simply dummy text of the printing and typesetting industry, used as standard filler since the early days of print. It has survived many decades and the leap into electronic layout, remaining essentially unchanged.</div>
  <svg class="abs" style="left:27px;top:92px" width="110" height="60" viewBox="0 0 110 60">
    <circle cx="7" cy="7" r="6" fill="var(--deep)"/><circle cx="7" cy="28" r="6" fill="var(--mint)"/><circle cx="7" cy="49" r="6" fill="var(--lime)"/>
    <g font-family="Roboto,sans-serif" fill="#fff" font-size="4" text-anchor="middle"><text x="7" y="8.5">1</text><text x="7" y="29.5">2</text><text x="7" y="50.5">3</text></g>
    <g font-family="Roboto Condensed,sans-serif" font-size="2.8"><text x="21" y="3" font-weight="700" fill="#333">Business Solutions #1</text><text x="21" y="24" font-weight="700" fill="#333">Business Solutions #1</text><text x="21" y="45" font-weight="700" fill="#333">Business Solutions #1</text>
    <g fill="#8a9096"><text x="21" y="7">Lorem ipsum is simply dummy text of the printing</text><text x="21" y="11">and typesetting industry. Lorem ipsum has been</text><text x="21" y="28">Lorem ipsum is simply dummy text of the printing</text><text x="21" y="32">and typesetting industry. Lorem ipsum has been</text><text x="21" y="49">Lorem ipsum is simply dummy text of the printing</text><text x="21" y="53">and typesetting industry. Lorem ipsum has been</text></g></g>
  </svg>
  <svg class="abs" style="left:160px;top:52px" width="145" height="105" viewBox="0 0 145 105">
    <text x="85" y="4" text-anchor="middle" font-size="4" font-family="Roboto,sans-serif" fill="#444">Title dummy text</text>
    <text x="85" y="9" text-anchor="middle" font-size="2.8" font-family="Roboto Condensed,sans-serif" fill="#8a9096">Lorem ipsum is simply dummy text</text>
    <g class="axis" text-anchor="end"><text x="8" y="24">35</text><text x="8" y="34">30</text><text x="8" y="44">25</text><text x="8" y="54">20</text><text x="8" y="64">15</text><text x="8" y="74">10</text><text x="8" y="84">5</text><text x="8" y="94">0</text></g>
    <path d="M15,34 L60,44 L80,30 L110,42 L128,64 L134,88 L130,92 L115,80 L95,68 Z" fill="#3aa32c"/>
    <path d="M20,28 L55,30 L80,34 L110,48 L138,66 L136,86 Z" fill="var(--lime)"/>
    <path d="M90,62 L115,48 L135,58 L138,80 L120,84 Z" fill="var(--mint)"/>
    <path d="M12,30 L50,36 L75,44 L95,60 L120,70 L130,82 L12,84 Z" fill="var(--deep)"/>
    <path d="M130,82 L138,78 L138,90 L130,92 Z" fill="#063026"/>
    <g class="axis" text-anchor="middle"><text x="12" y="100">1/5/2002</text><text x="43" y="102">1/6/2002</text><text x="74" y="103">1/7/2002</text><text x="105" y="104">1/8/2002</text><text x="134" y="105">1/9/2002</text></g>
  </svg>
  <div class="footer"><span class="brand">NOVALYNE</span><span class="link">brand page/novalyne</span><span class="num">12</span></div>
</section>

<!-- 13 bar chart -->
<section class="slide" style="left:56px;top:931px">
  <div class="mark"><i></i>NOVALYNE</div>
  <h2 class="title" style="left:25px;top:30px">Title for Data Bar Slide<br>Service and Solutions.</h2>
  <div class="text" style="left:25px;top:61px;width:110px">Lorem ipsum is simply dummy text of the printing and typesetting industry, used as standard filler since the early days of print. It has survived many decades and the leap into electronic layout, remaining essentially unchanged. It was made popular with sheets of transfer letters and later with desktop publishing software.</div>
  <ul class="bullets" style="left:25px;top:112px;width:110px">
    <li>It is a long established fact that a reader will be distracted by the readable content of a page.</li>
    <li>The point of using it is a more or less normal distribution of letters, making it look readable.</li>
    <li>Many publishing packages now use it as their default model text.</li>
  </ul>
  <svg class="abs" style="left:160px;top:52px" width="140" height="100" viewBox="0 0 140 100">
    <g class="axis" text-anchor="end"><text x="6" y="6">5</text><text x="6" y="15">4.5</text><text x="6" y="24">4</text><text x="6" y="33">3.5</text><text x="6" y="43">3</text><text x="6" y="52">2.5</text><text x="6" y="61">2</text><text x="6" y="70">1.5</text><text x="6" y="80">1</text><text x="6" y="89">0.5</text><text x="6" y="98">0</text></g>
    <line x1="10" y1="97" x2="136" y2="97" stroke="#ccc" stroke-width=".4"/>
    <rect x="15" y="17" width="20" height="80" fill="var(--deep)"/>
    <rect x="47" y="51" width="20" height="46" fill="var(--mint)"/>
    <rect x="79" y="32" width="20" height="65" fill="var(--slate)"/>
    <rect x="111" y="13" width="20" height="84" fill="var(--gray)"/>
  </svg>
  <svg class="abs" style="left:160px;top:150px" width="140" height="8"><g class="axis" text-anchor="middle"><text x="25" y="4">Solutions</text><text x="57" y="4">Design</text><text x="89" y="4">Promotion</text><text x="121" y="4">Consulting</text></g></svg>
  <div class="footer"><span class="brand">NOVALYNE</span><span class="link">brand page/novalyne</span><span class="num">13</span></div>
</section>

<!-- 14 pie & bar -->
<section class="slide" style="left:443px;top:931px">
  <div class="mark"><i></i>NOVALYNE</div>
  <h2 class="title" style="left:27px;top:30px">Title for Data Pie &amp; Bar<br>Service and Solutions.</h2>
  <div class="text" style="left:150px;top:30px;width:148px">Lorem ipsum is simply dummy text of the printing and typesetting industry, used as standard filler since the early days of print. It has survived many decades and the leap into electronic layout, remaining essentially unchanged. It was made popular with sheets of transfer letters and later with desktop publishing software.</div>
  <svg class="abs" style="left:25px;top:64px" width="120" height="100" viewBox="0 0 120 100">
    <circle cx="27" cy="27" r="22" fill="none" stroke="var(--slate)" stroke-width="4"/>
    <path d="M27,5 A22,22 0 0 1 44,13" fill="none" stroke="#d5d9dc" stroke-width="4"/>
    <circle cx="96" cy="27" r="22" fill="none" stroke="var(--slate)" stroke-width="4"/>
    <path d="M96,5 A22,22 0 0 1 117,24" fill="none" stroke="var(--mint)" stroke-width="4"/>
    <g font-family="Roboto Condensed,sans-serif" text-anchor="middle"><text x="27" y="28" font-size="5" fill="#555">15% / 20%</text><text x="27" y="33" font-size="2.6" fill="#999">$18,258,250</text><text x="96" y="28" font-size="5" fill="#555">30% / 20%</text><text x="96" y="33" font-size="2.6" fill="#999">$18,258,250</text></g>
    <circle cx="4" cy="64" r="2.5" fill="var(--deep)"/><path d="M2.8,64 L3.8,65 L5.4,63" stroke="#fff" stroke-width=".6" fill="none"/>
    <circle cx="4" cy="84" r="2.5" fill="var(--deep)"/><path d="M2.8,84 L3.8,85 L5.4,83" stroke="#fff" stroke-width=".6" fill="none"/>
    <g font-family="Roboto Condensed,sans-serif" font-size="2.8" fill="#8a9096"><text x="13" y="63">Objectively disintermediate leveraged manufactured products</text><text x="13" y="67">before team driven resources.</text><text x="13" y="83">Objectively disintermediate leveraged manufactured products</text><text x="13" y="87">before team driven resources.</text></g>
  </svg>
  <svg class="abs" style="left:163px;top:69px" width="135" height="88" viewBox="0 0 135 88">
    <g class="axis" text-anchor="end"><text x="4" y="3">7</text><text x="4" y="15">6</text><text x="4" y="27">5</text><text x="4" y="39">4</text><text x="4" y="50">3</text><text x="4" y="62">2</text><text x="4" y="74">1</text><text x="4" y="86">0</text></g>
    <g stroke="#e6e6e6" stroke-width=".3"><line x1="7" y1="2" x2="135" y2="2"/><line x1="7" y1="14" x2="135" y2="14"/><line x1="7" y1="26" x2="135" y2="26"/><line x1="7" y1="38" x2="135" y2="38"/><line x1="7" y1="49" x2="135" y2="49"/><line x1="7" y1="61" x2="135" y2="61"/><line x1="7" y1="73" x2="135" y2="73"/></g>
    <g fill="var(--slate)"><rect x="10" y="83" width="6" height="3"/><rect x="22" y="80" width="6" height="6"/><rect x="34" y="76" width="6" height="10"/><rect x="46" y="62" width="6" height="24"/><rect x="58" y="60" width="6" height="26"/><rect x="70" y="40" width="6" height="46"/><rect x="82" y="44" width="6" height="42"/><rect x="94" y="54" width="6" height="32"/><rect x="106" y="34" width="6" height="52"/><rect x="118" y="70" width="6" height="16"/></g>
    <g fill="var(--mint)"><rect x="10" y="82" width="6" height="1"/><rect x="22" y="78" width="6" height="2"/><rect x="34" y="72" width="6" height="4"/><rect x="46" y="52" width="6" height="10"/><rect x="58" y="50" width="6" height="10"/><rect x="70" y="30" width="6" height="10"/><rect x="82" y="16" width="6" height="28"/><rect x="94" y="20" width="6" height="34"/><rect x="106" y="24" width="6" height="10"/><rect x="118" y="64" width="6" height="6"/></g>
  </svg>
  <div class="footer"><span class="brand">NOVALYNE</span><span class="link">brand page/novalyne</span><span class="num">14</span></div>
</section>

<!-- 15 horizontal bars -->
<section class="slide" style="left:826px;top:931px">
  <div class="mark"><i></i>NOVALYNE</div>
  <svg class="abs" style="left:22px;top:22px" width="130" height="145" viewBox="0 0 130 145">
    <line x1="15" y1="4" x2="15" y2="130" stroke="#ccc" stroke-width=".4"/>
    <g class="axis" text-anchor="end"><text x="12" y="19">2024</text><text x="12" y="50">2023</text><text x="12" y="82">2022</text><text x="12" y="113">2021</text></g>
    <rect x="15" y="8" width="37" height="8" fill="var(--slate)"/><rect x="15" y="18" width="48" height="8" fill="var(--mint)"/>
    <rect x="15" y="39" width="64" height="8" fill="var(--slate)"/><rect x="15" y="49" width="48" height="8" fill="var(--mint)"/>
    <rect x="15" y="71" width="21" height="8" fill="var(--slate)"/><rect x="15" y="81" width="90" height="8" fill="var(--lime)"/>
    <rect x="15" y="102" width="48" height="8" fill="var(--slate)"/><rect x="15" y="112" width="80" height="8" fill="var(--deep)"/>
    <g class="axis" text-anchor="middle"><text x="15" y="138">0</text><text x="36" y="138">20</text><text x="57" y="138">40</text><text x="78" y="138">60</text><text x="99" y="138">80</text><text x="120" y="138">100</text></g>
  </svg>
  <div class="abs" style="left:150px;top:22px;width:.5px;height:135px;background:#e2e2e2"></div>
  <h2 class="title" style="left:162px;top:35px">Title for Data Bar Slide<br>Service and Solutions.</h2>
  <div class="text" style="left:162px;top:62px;width:136px">Lorem ipsum is simply dummy text of the printing and typesetting industry, used as standard filler since the early days of print. It has survived many decades and the leap into electronic layout, remaining essentially unchanged. It was made popular with sheets of transfer letters and later with desktop publishing software.</div>
  <div class="abs" style="left:162px;top:112px;font-size:3.6px;font-weight:700">Chart Descriptions</div>
  <div class="text" style="left:162px;top:118px;width:136px">Lorem ipsum is simply dummy text of the printing and typesetting industry, used as standard filler since the early days of print.</div>
  <div class="abs" style="left:162px;top:141px;display:flex;gap:10px;font-family:'Roboto Condensed',sans-serif;font-size:2.6px;color:#fff">
    <span style="background:var(--deep);padding:1px 3px">Data #1</span><span style="background:var(--mint);padding:1px 3px">Data #1</span><span style="background:var(--mint);padding:1px 3px">Data #1</span><span style="background:var(--lime);padding:1px 3px">Data #1</span><span style="background:var(--slate);padding:1px 3px">Data #1</span>
  </div>
  <div class="footer"><span class="brand">NOVALYNE</span><span class="link">brand page/novalyne</span><span class="num">15</span></div>
</section>

</body>
</html>
```